Seminarübersicht für Jobcenter
Zielgruppe
Meine Firma heißt 'Arbeitsbrückenwerk.de' und berät Grundhilfe B Jobcenter bei der Beschleunigung von Vermittlungserfolgen. Das Besondere an unserem Konzept ist, dass die Beratung in Seminarform erfolgt und nicht über Arbeitslose spricht, sondern in diesen Seminaren MIT den Arbeitslosen arbeitet. Diese Innovation ist ein absolutes Alleinstellungsmerkmal, da wir im Beisein von Jobcenter-Mitarbeitern und arbeitslosen Teilnehmern mit den echten Bewerbungsunterlagen arbeiten, auf die individuellen Belange der Teilnehmer eingehen und DIREKT aus dem SEMINAR heraus vermitteln: wir hakren bei Arbeitgebern bei ausbleibenden Reaktionen oder bei abschlägig beschiedenen Bewerbungen nach, akquirieren Stellen für die langzeitarbeitslosen Teilnehmer und formen gemeinsam eine Strategie und einen Zeitplan für den Wiedereinstieg in Arbeit. Die Erfolge und Resonanzen aus unseren bisherig besuchten Jobcentern sind sensationell.
Aufgabenstellung
Flyer mit einer Übersicht für die verschiedenen Seminarangebote:
IDEENTAG(1-Tages-Veranstaltung) Inspirationen zu Akquise-, Bewerbungsmöglichkeiten (Vortragsform)
MOTIVATIONSTAGE(2-Tagesveranstaltung) ergänzt den Ideentag um das Einbinden der Teilnehmer. Einbinden der individuellen Belange in Workshopform, Ausprobieren den Praxis mit live Arbeitgeberakquise
AKTIVIERUNGSTAGE (3-Tages-Veranstaltung) ergänzt die Motivationstage um eine mehrwöchige (betreute) Umsetzungsphase und ein Einzel- bzw. Kleingruppencoaching
VERMITTLUNGSTAGE (5-Tages-Veranstaltung) ergänzt die Aktivierungstage um eine weitere Umsetzungsphase nach den Einzelgesprächen, einen Gruppen-Auswertungstag mit weiterer Umsetzungsphase und abschließendem Einzelgespräch als 5.Veranstaltungstag.
Dazu bieten wir für Jobcenter begleitend Themenseminare an (Rhetorik und Körpersprache im Vermittlungsgespräch, Motivation und Zielgespräche im Bewerbergespräch)
Die Grundfarben meiner Firma sind violett und orange.
Für ein schickes neues Outfit bin ich bereit, den bisherigen Marktauftritt anzupassen.

```html
<!DOCTYPE html>
<html lang="de">
<head>
<meta charset="utf-8">
<title>Arbeitsbrückenwerk.de – Seminarübersicht</title>
<link rel="stylesheet" href="https://fonts.googleapis.com/css2?family=Open+Sans:wght@400;600;700;800&display=swap">
<style>
  :root {
    --stage: #3f393a;
    --violet: #7d4f96;
    --violet-deep: #5b3377;
    --orange: #f0a81c;
    --orange-deep: #e3941a;
    --coral: #ef5f4e;
    --sand: #f4d6a2;
    --white: #ffffff;
    --font: "Open Sans", Arial, sans-serif;
  }
  * { box-sizing: border-box; margin: 0; padding: 0; }
  html, body { width: 1200px; height: 888px; overflow: hidden; }
  body { background: var(--stage); font-family: var(--font); color: var(--white); }

  .canvas { position: relative; width: 1200px; height: 888px; }

  .flyer {
    position: absolute; left: 160px; width: 880px; height: 410px;
    overflow: hidden; background: var(--orange);
  }
  .flyer--front { top: 24px; }
  .flyer--back { top: 454px; }

  /* ---------- Front side ---------- */
  .front-header {
    position: absolute; left: 0; top: 0; width: 320px; height: 410px;
    background: linear-gradient(160deg, var(--violet) 0%, var(--violet-deep) 100%);
  }
  .front-title {
    position: absolute; left: 34px; top: 26px;
    font-size: 34px; line-height: 34px; font-weight: 800; text-transform: uppercase;
    letter-spacing: 0.5px;
  }
  .front-illustration {
    position: absolute; left: 0; top: 160px; width: 320px; height: 250px;
    background: linear-gradient(135deg, var(--sand) 0%, var(--coral) 70%, var(--violet-deep) 100%);
  }
  .offers {
    position: absolute; left: 360px; top: 34px; width: 490px;
    display: grid; grid-template-columns: 1fr 1fr; column-gap: 34px; row-gap: 30px;
  }
  .offer__badge {
    display: inline-block; background: var(--violet-deep);
    font-size: 10px; font-weight: 600; padding: 1px 5px; text-transform: uppercase;
  }
  .offer__title {
    font-size: 23px; font-weight: 800; text-transform: uppercase; line-height: 1.1; margin: 4px 0 6px;
  }
  .offer__text { font-size: 11.5px; line-height: 1.45; }
  .expert-tip {
    position: absolute; left: 360px; bottom: 26px; width: 490px;
    font-size: 12.5px; font-weight: 700;
  }

  /* ---------- Back side ---------- */
  .back-body {
    position: absolute; left: 0; top: 0; width: 620px; height: 300px;
    background: linear-gradient(160deg, var(--violet) 0%, var(--violet-deep) 100%);
    padding: 34px 40px;
  }
  .back-title {
    font-size: 38px; line-height: 40px; font-weight: 800; text-transform: uppercase;
  }
  .back-text { margin-top: 18px; font-size: 12px; line-height: 1.55; max-width: 520px; }
  .back-contact {
    position: absolute; left: 0; top: 300px; width: 620px; height: 110px;
    padding: 28px 40px; background: var(--orange);
  }
  .brand { font-size: 15px; font-weight: 700; text-transform: uppercase; }
  .address { margin-top: 6px; font-size: 12px; }
  .back-illustration {
    position: absolute; left: 620px; top: 0; width: 260px; height: 410px;
    background: linear-gradient(200deg, var(--violet-deep) 0%, var(--coral) 55%, var(--sand) 100%);
  }
</style>
</head>
<body>
<main class="canvas">

  <section class="flyer flyer--front">
    <div class="front-header">
      <h1 class="front-title">Unsere<br>Seminar<br>Angebote</h1>
      <div class="front-illustration" role="img" aria-label="Illustration: Person blickt durch ein Fernglas"></div>
    </div>

    <div class="offers">
      <article class="offer">
        <span class="offer__badge">1 Tag</span>
        <h2 class="offer__title">Ideentag</h2>
        <p class="offer__text">Lorem ipsum dolor sit amet, consetetur sadipscing elitr, sed diam nonumy eirmod tempor invidunt ut labore et dolore magna aliquyam erat, sed diam voluptua.</p>
      </article>
      <article class="offer">
        <span class="offer__badge">2 Tage</span>
        <h2 class="offer__title">Motivationstage</h2>
        <p class="offer__text">At vero eos et accusam et justo duo dolores et ea rebum. Stet clita kasd gubergren, no sea takimata sanctus est Lorem ipsum dolor sit amet.</p>
      </article>
      <article class="offer">
        <span class="offer__badge">3 Tage</span>
        <h2 class="offer__title">Aktivierungstage</h2>
        <p class="offer__text">At vero eos et accusam et justo duo dolores et ea rebum. Stet clita kasd gubergren, no sea takimata sanctus est Lorem ipsum dolor sit amet.</p>
      </article>
      <article class="offer">
        <span class="offer__badge">5 Tage</span>
        <h2 class="offer__title">Vermittlungstage</h2>
        <p class="offer__text">Lorem ipsum dolor sit amet, consetetur sadipscing elitr, sed diam nonumy eirmod tempor invidunt ut labore et dolore magna aliquyam erat, sed diam voluptua.</p>
      </article>
    </div>

    <p class="expert-tip">Experten-Tipp: Kombinieren Sie alle 4 Seminare zu einem 2-wöchigen Intensivtraining!</p>
  </section>

  <section class="flyer flyer--back">
    <div class="back-body">
      <h2 class="back-title">Die Vermittlung<br>es jetzt angehen</h2>
      <p class="back-text">Eirmod tempor invidunt ut labore et dolore magna aliquyam erat, sed diam voluptua. At vero eos et accusam et justo duo dolores et ea rebum. Stet clita kasd gubergren, no sea takimata sanctus est.<br>Dazu bieten wir begleitend Themenseminare an (Rhetorik und Körpersprache im Vermittlungsgespräch, Motivation und Zielgespräche im Bewerbergespräch).</p>
    </div>
    <div class="back-contact">
      <p class="brand">Arbeitsbrückenwerk.de</p>
      <p class="address">Lena Harbeck | Am Lindenhang 12 | 07999 Musterau | Tel.: 03601/ 23 45 67</p>
    </div>
    <div class="back-illustration" role="img" aria-label="Illustration: Person blickt durch ein Fernglas"></div>
  </section>

</main>
</body>
</html>
```